Wageline Associates Business Card Design

We need a business card designed around our new logo. The business card should be modern in design & should communicate success, confidence, power, sophistication. The target market is young business professionals. This is for a human resource & payroll outsourcing business.

```html
<!DOCTYPE html>
<html lang="en">
<head>
<meta charset="utf-8">
<title>Wageline Associates – Business Card</title>
<link rel="stylesheet" href="https://fonts.googleapis.com/css2?family=Poppins:wght@400;600&display=swap">
<style>
  :root {
    --backdrop: #3a4049;
    --card: #ffffff;
    --ink: #111111;
    --muted: #6b6b6b;
    --accent: #e81c24;
    --night: #07080b;
  }
  * { margin: 0; padding: 0; box-sizing: border-box; }
  html, body { width: 1200px; height: 1000px; overflow: hidden; }
  body {
    background: var(--backdrop);
    font-family: "Poppins", sans-serif;
    position: relative;
  }
  .card {
    position: absolute;
    left: 100px; top: 215px;
    width: 1000px; height: 570px;
    background: var(--card);
    border-radius: 28px;
    overflow: hidden;
  }
  .card__corner { position: absolute; inset: 0; }
  .brand {
    position: absolute;
    left: 230px; top: 78px;
    display: flex; align-items: center; gap: 14px;
  }
  .brand__dot {
    width: 22px; height: 22px; border-radius: 50%;
    background: var(--accent);
  }
  .brand__name {
    font-size: 40px; font-weight: 600; color: var(--ink);
    letter-spacing: 0.5px;
  }
  .identity__bar {
    position: absolute; left: 150px; top: 200px;
    width: 16px; height: 74px; background: var(--accent);
  }
  .identity {
    position: absolute; left: 188px; top: 196px;
  }
  .identity__name {
    font-size: 40px; font-weight: 600; color: var(--accent); line-height: 1.1;
  }
  .identity__role {
    font-size: 27px; font-weight: 400; color: var(--ink); line-height: 1.3;
  }
  .address {
    position: absolute; left: 188px; top: 300px;
    font-size: 22px; color: var(--muted); line-height: 1.35;
    font-style: normal;
  }
  .contacts {
    position: absolute; left: 150px; top: 380px;
    list-style: none;
  }
  .contacts__item {
    display: flex; align-items: center; gap: 16px;
    font-size: 22px; color: var(--muted); line-height: 1.5;
  }
  .contacts__icon { width: 20px; height: 20px; flex: none; }
</style>
</head>
<body>
  <article class="card">
    <svg class="card__corner" viewBox="0 0 1000 570" aria-hidden="true">
      <path d="M560 570 C 780 560 930 430 1000 170 L1000 570 Z" fill="var(--night)"/>
      <path d="M540 570 C 760 555 905 425 975 170 L1000 170 C 930 430 780 560 560 570 Z" fill="var(--accent)"/>
      <path d="M556 570 C 776 558 920 428 990 170" fill="none" stroke="#ffffff" stroke-width="3"/>
    </svg>

    <div class="brand">
      <span class="brand__dot"></span>
      <span class="brand__name">Wageline Associates</span>
    </div>

    <span class="identity__bar"></span>
    <header class="identity">
      <h1 class="identity__name">Marten Coles</h1>
      <p class="identity__role">General Manager</p>
    </header>

    <address class="address">
      Hollis Crossing<br>
      Vandermere Park, 1620
    </address>

    <ul class="contacts">
      <li class="contacts__item">
        <svg class="contacts__icon" viewBox="0 0 24 24"><path fill="var(--accent)" d="M6.6 10.8a15 15 0 0 0 6.6 6.6l2.2-2.2c.3-.3.7-.4 1-.2 1.1.4 2.3.6 3.6.6.6 0 1 .4 1 1V20c0 .6-.4 1-1 1A17 17 0 0 1 3 4c0-.6.4-1 1-1h3.5c.6 0 1 .4 1 1 0 1.3.2 2.5.6 3.6.1.3 0 .7-.2 1z"/></svg>
        02 5550 1870
      </li>
      <li class="contacts__item">
        <svg class="contacts__icon" viewBox="0 0 24 24"><rect x="6" y="2" width="12" height="20" rx="2" fill="none" stroke="var(--accent)" stroke-width="2.4"/><circle cx="12" cy="18" r="1.3" fill="var(--accent)"/></svg>
        0412 555 019
      </li>
      <li class="contacts__item">
        <svg class="contacts__icon" viewBox="0 0 24 24"><rect x="2" y="5" width="20" height="14" rx="1.5" fill="var(--accent)"/><path d="M3 6l9 7 9-7" fill="none" stroke="#fff" stroke-width="2"/></svg>
        contact@wageline.com.au
      </li>
      <li class="contacts__item">
        <svg class="contacts__icon" viewBox="0 0 24 24"><circle cx="12" cy="12" r="10" fill="var(--accent)"/><path d="M2 12h20M12 2c3 3 3 17 0 20M12 2c-3 3-3 17 0 20" fill="none" stroke="#fff" stroke-width="1.5"/></svg>
        www.wageline-hr.com
      </li>
    </ul>
  </article>
</body>
</html>
```